Business Card - Cooperate

Business Card for Larkfield Management Consulting

Target Market(s)

Corparte - b2B

Industry/Entity Type

Management Consulting - Professional Services

Contact Information for Business Card

Company Name , Slogan , Dummy Address,

Requirements
Must have
• Grow Beyond Your Limits

```html
<!DOCTYPE html>
<html lang="en">
<head>
<meta charset="utf-8">
<title>Larkfield Management Consulting – Business Card</title>
<link rel="stylesheet" href="https://fonts.googleapis.com/css2?family=Lato:wght@400;700;900&display=swap">
<style>
  :root {
    --stage: #05080d;
    --paper: #ececec;
    --paper-shade: #dcdcdc;
    --navy: #1a1f7a;
    --blue: #1c64d8;
    --blue-deep: #1a5cc4;
    --green: #2fb412;
    --lime: #6ccf1a;
    --slogan: #2a9a4a;
    --white: #ffffff;
  }
  * { box-sizing: border-box; margin: 0; padding: 0; }
  html, body {
    width: 1200px; height: 958px; overflow: hidden;
    background: var(--stage);
    font-family: "Lato", sans-serif;
  }
  .canvas {
    width: 1200px; height: 958px;
    display: flex; flex-direction: column; align-items: center; justify-content: center;
    gap: 30px;
  }
  .card {
    position: relative;
    width: 760px; height: 434px;
    border-radius: 4px; overflow: hidden;
  }

  /* Front */
  .card--front { background: linear-gradient(160deg, var(--paper) 0%, var(--paper-shade) 60%, var(--paper) 100%); }
  .card__band { position: absolute; inset: 0; }
  .brand { position: absolute; top: 72px; left: 0; width: 100%; display: flex; justify-content: center; align-items: center; gap: 20px; }
  .brand__dot { width: 62px; height: 62px; border-radius: 50%; background: var(--blue); }
  .brand__text { display: flex; flex-direction: column; }
  .brand__name { font-weight: 900; font-size: 58px; line-height: 1; color: var(--navy); letter-spacing: 1px; }
  .brand__slogan { margin-top: 8px; font-weight: 700; font-size: 13px; letter-spacing: 3.2px; color: var(--slogan); text-transform: uppercase; white-space: nowrap; }

  .person { position: absolute; top: 278px; right: 415px; text-align: right; color: var(--white); white-space: nowrap; }
  .person__name { font-weight: 900; font-size: 25px; }
  .person__role { font-size: 15px; margin-top: 2px; }
  .person__address { font-weight: 700; font-size: 16px; margin-top: 14px; line-height: 1.35; }

  .divider { position: absolute; left: 370px; top: 278px; width: 1.5px; height: 122px;
    background: linear-gradient(180deg, rgba(255,255,255,0), rgba(255,255,255,.85) 50%, rgba(255,255,255,0)); }

  .contact { position: absolute; left: 394px; top: 306px; list-style: none; color: var(--white); font-size: 16px; white-space: nowrap; }
  .contact__item { display: flex; align-items: center; gap: 10px; height: 28px; }
  .contact__icon { width: 20px; height: 20px; flex: none; }

  /* Back */
  .card--back { background: linear-gradient(105deg, var(--blue-deep) 0%, var(--blue) 42%, #2a9a40 72%, var(--green) 100%); }
  .back__ring { position: absolute; left: 150px; top: 40px; width: 330px; height: 330px; border-radius: 50%; background: rgba(255,255,255,.22); }
  .back__brand { position: absolute; left: 180px; top: 140px; display: flex; flex-direction: column; }
  .back__name { font-weight: 900; font-size: 74px; line-height: 1; color: var(--white); letter-spacing: 2px; }
  .back__slogan { margin-top: 10px; font-weight: 700; font-size: 15px; letter-spacing: 4px; color: var(--white); text-transform: uppercase; white-space: nowrap; }
  .back__web { position: absolute; right: 30px; bottom: 26px; font-size: 14px; letter-spacing: 4px; color: var(--white); }
</style>
</head>
<body>
<main class="canvas">

  <section class="card card--front" aria-label="Business card front">
    <svg class="card__band" width="760" height="434" viewBox="0 0 760 434" aria-hidden="true">
      <defs>
        <linearGradient id="bandFill" x1="0" y1="0" x2="1" y2="0.25">
          <stop offset="0" stop-color="#1a5cc4"/>
          <stop offset="0.5" stop-color="#1c6ae0"/>
          <stop offset="0.78" stop-color="#3f9f6a"/>
          <stop offset="1" stop-color="#6ccf1a"/>
        </linearGradient>
      </defs>
      <path d="M0 246 H360 L374 262 L388 246 H760 V434 H0 Z" fill="url(#bandFill)"/>
    </svg>

    <div class="brand">
      <span class="brand__dot"></span>
      <div class="brand__text">
        <span class="brand__name">larkfield</span>
        <span class="brand__slogan">Grow beyond your limits</span>
      </div>
    </div>

    <div class="person">
      <p class="person__name">Dana Whitlock</p>
      <p class="person__role">Technology Specialist</p>
      <p class="person__address">1720 Meadow Lane<br>Fairview, MO 63000</p>
    </div>

    <span class="divider"></span>

    <ul class="contact">
      <li class="contact__item">
        <svg class="contact__icon" viewBox="0 0 20 20"><circle cx="10" cy="10" r="10" fill="#fff"/><path d="M5 8.5c0-1.5 2.2-2.5 5-2.5s5 1 5 2.5l-1.6.6-.6-1.4H7.2l-.6 1.4zM7 9.5h6l1 4.5H6z" fill="#1c64d8"/></svg>
        <span>555-202-0147</span>
      </li>
      <li class="contact__item">
        <svg class="contact__icon" viewBox="0 0 20 20"><circle cx="10" cy="10" r="10" fill="#fff"/><rect x="7" y="4.5" width="6" height="11" rx="1.2" fill="none" stroke="#1c64d8" stroke-width="1.4"/><circle cx="10" cy="13.3" r=".8" fill="#1c64d8"/></svg>
        <span>555.884.0199</span>
      </li>
      <li class="contact__item">
        <svg class="contact__icon" viewBox="0 0 20 20"><circle cx="10" cy="10" r="10" fill="#fff"/><rect x="5" y="6.5" width="10" height="7" fill="none" stroke="#1c64d8" stroke-width="1.3"/><path d="M5 6.5l5 4 5-4" fill="none" stroke="#1c64d8" stroke-width="1.3"/></svg>
        <span>dana.whitlock@larkfieldmc.com</span>
      </li>
    </ul>
  </section>

  <section class="card card--back" aria-label="Business card back">
    <span class="back__ring"></span>
    <div class="back__brand">
      <span class="back__name">larkfield</span>
      <span class="back__slogan">Grow beyond your limits</span>
    </div>
    <p class="back__web">www.larkfield.com</p>
  </section>

</main>
</body>
</html>
```